Kettle Ledger Business Card design

We need a stand out business card design for Accounting practice based in Australia specialising in pubs, clubs and hotels. We help venues maximise margins, create time and manage cashflow. One club we have been working with for the last 6 months has increased revenue by 3% and margin by 5% in this time frame. We have a back office outsourced system that costs less than having a full time employee and also allows the venues the added benefit of:<br/>-using the office space to become a revenue generating opportunity. <br/>-a complete system to enhance governance, accountability and efficiency within their operation<br/>-52 weeks cover so no hassle to cover annual/sick .. leave<br/><br/>We would like to see designs that use the colours of our logo (green & blue).
Target Market(s)
Australian Pubs, Clubs & Hotels abookkeeping, accounting and tax services
Industry/Entity Type
Accountant
Contact Information for Business Card
Miriam Oakley CPA
Principal
Accountant Tax Agent
Miriam@KettleLedger-example.com.au
0418693142
www.kettleledger-example.com.au
Accounting / Payroll / Tax / SMSF / Technology
Colors
Designer to choose colors to be used in the design.
Look and feel
Each slider illustrates characteristics of the customer's brand and the style your logo design should communicate.

```html
<!DOCTYPE html>
<html lang="en">
<head>
<meta charset="utf-8">
<title>Kettle Ledger – Business Card</title>
<link rel="stylesheet" href="https://fonts.googleapis.com/css2?family=Poppins:ital,wght@0,400;0,500;0,700;0,800;1,400;1,600;1,700&display=swap">
<style>
  :root {
    --brand-blue: #27409a;
    --brand-green: #137a43;
    --card-white: #ffffff;
    --card-shade: #f1f2f4;
    --stage: #e6e7ea;
    --ink-faint: #e4e5ef;
  }
  * { margin: 0; padding: 0; box-sizing: border-box; }
  html, body {
    width: 1200px; height: 900px; overflow: hidden;
    background: var(--stage);
    font-family: "Poppins", sans-serif;
  }
  .sheet {
    position: relative; width: 1200px; height: 900px;
  }
  .card {
    position: absolute; left: 250px; width: 700px; height: 400px;
    background: linear-gradient(135deg, var(--card-white) 0%, var(--card-shade) 100%);
    box-shadow: 0 10px 28px rgba(0,0,0,0.18);
    overflow: hidden;
  }
  .card--front { top: 40px; }
  .card--back { top: 480px; }

  /* wordmark */
  .wordmark {
    color: var(--brand-blue);
    font-weight: 800;
    letter-spacing: -1px;
    line-height: 1;
  }

  /* front */
  .card--front .wordmark {
    position: absolute; left: 48px; top: 44px; font-size: 58px;
  }
  .contact-block {
    position: absolute; left: 48px; top: 150px;
    color: var(--brand-blue);
  }
  .contact-block .person {
    font-weight: 700; font-style: italic; font-size: 21px;
  }
  .contact-block .role {
    color: var(--brand-green); font-style: italic; font-size: 14px; line-height: 1.35;
    margin-bottom: 14px;
  }
  .contact-list { list-style: none; font-size: 14px; }
  .contact-list li {
    display: flex; align-items: center; gap: 9px; margin-bottom: 6px;
  }
  .contact-list svg { width: 14px; height: 14px; fill: var(--brand-green); flex: none; }
  .green-panel {
    position: absolute; right: 0; bottom: 0; width: 270px; height: 250px;
    background: var(--brand-green);
  }

  /* back */
  .card--back .wordmark {
    position: absolute; left: 180px; top: 100px; font-size: 64px;
  }
  .card--back .mark-dot {
    position: absolute; left: 110px; top: 106px; width: 52px; height: 52px;
    border-radius: 50%; background: var(--brand-green);
  }
  .services {
    position: absolute; left: 0; right: 0; bottom: 62px;
    display: flex; justify-content: center; align-items: center; gap: 14px;
    color: var(--brand-blue); font-size: 17px; font-weight: 500;
    list-style: none;
  }
  .services li + li::before {
    content: ""; display: inline-block; width: 8px; height: 8px; border-radius: 50%;
    background: var(--brand-green); margin-right: 14px; vertical-align: middle;
  }
  .web-band {
    position: absolute; left: 0; right: 0; bottom: 16px; height: 36px;
    background: var(--brand-blue); color: var(--card-white);
    display: flex; align-items: center; justify-content: center;
    font-size: 15px; letter-spacing: 0.5px;
  }
</style>
</head>
<body>
<main class="sheet">

  <section class="card card--front" aria-label="Business card front">
    <div class="wordmark">Kettle Ledger</div>
    <div class="contact-block">
      <p class="person">Miriam Oakley CPA</p>
      <p class="role">Principal<br>Accountant Tax Agent</p>
      <ul class="contact-list">
        <li>
          <svg viewBox="0 0 24 24" aria-hidden="true"><path d="M6.6 10.8a15.1 15.1 0 0 0 6.6 6.6l2.2-2.2a1 1 0 0 1 1-.25 11.4 11.4 0 0 0 3.6.57 1 1 0 0 1 1 1V20a1 1 0 0 1-1 1A17 17 0 0 1 3 4a1 1 0 0 1 1-1h3.5a1 1 0 0 1 1 1c0 1.25.2 2.45.57 3.57a1 1 0 0 1-.25 1z"/></svg>
          0418693142
        </li>
        <li>
          <svg viewBox="0 0 24 24" aria-hidden="true"><path d="M2 5h20v14H2z M4 7v.4l8 5.2 8-5.2V7z" fill-rule="evenodd"/></svg>
          Miriam@KettleLedger-example.com.au
        </li>
        <li>
          <svg viewBox="0 0 24 24" aria-hidden="true"><path d="M12 2a10 10 0 1 0 0 20 10 10 0 0 0 0-20zm6.9 6h-3a15.7 15.7 0 0 0-1.3-3.9A8 8 0 0 1 18.9 8zM12 4c.8 1.2 1.4 2.6 1.8 4h-3.6c.4-1.4 1-2.8 1.8-4zM4.3 14a8 8 0 0 1 0-4h3.4a16 16 0 0 0 0 4zm.8 2h3a15.7 15.7 0 0 0 1.3 3.9A8 8 0 0 1 5.1 16zm3-8h-3a8 8 0 0 1 4.3-3.9A15.7 15.7 0 0 0 8.1 8zM12 20c-.8-1.2-1.4-2.6-1.8-4h3.6c-.4 1.4-1 2.8-1.8 4zm2.3-6H9.7a14.7 14.7 0 0 1 0-4h4.6a14.7 14.7 0 0 1 0 4zm.3 5.9a15.7 15.7 0 0 0 1.3-3.9h3a8 8 0 0 1-4.3 3.9zm1.7-5.9a16 16 0 0 0 0-4h3.4a8 8 0 0 1 0 4z"/></svg>
          www.kettleledger-example.com.au
        </li>
      </ul>
    </div>
    <div class="green-panel" role="img" aria-label="Large brand emblem on green field"></div>
  </section>

  <section class="card card--back" aria-label="Business card back">
    <span class="mark-dot" aria-hidden="true"></span>
    <div class="wordmark">Kettle Ledger</div>
    <ul class="services">
      <li>Accounting</li>
      <li>Payroll</li>
      <li>Tax</li>
      <li>SMSF</li>
      <li>Technology</li>
    </ul>
    <div class="web-band">www.kettleledger-example.com.au</div>
  </section>

</main>
</body>
</html>
```